We need a full website with logo/graphics/woocommerce for hemp-based company

This site will be lunavetta.com. It is a website featuring the fact we are the only manufacturer to produce CBDP and THCP. It should be great on mobile and desktop. We will pay for any extensions needed and while it should be a simple site:

About Us
About the Laboratory
About CBDP
About THCP
Shop
Contact Us

Only 4 products on the site.

It can be wordpress or joomla. Your choice. You must install the final website on our server. We agree to pay for monthly support that must be submitted in your quote.

He have a great graphics designer that will assist keeping colors and graphics clean according to your specifications.

Industry/Entity Type

Hemp CBD THC

Coding

Coded - Design and coding required

Number of Pages Required

5+ page

Requirements
Must have
• A simple clean layout

```html
<!DOCTYPE html>
<html lang="en">
<head>
<meta charset="utf-8">
<title>Lunavetta</title>
<link href="https://fonts.googleapis.com/css2?family=Domine:wght@400;700&family=Lato:wght@400;700&display=swap" rel="stylesheet">
<style>
:root{
  --green:#1f8a4c;
  --green-dark:#156b39;
  --lime:#3ee86a;
  --ink:#111;
  --muted:#777;
  --line:#ddd;
  --gray-bg:#f1f1f1;
  --footer:#000;
}
*{box-sizing:border-box;margin:0;padding:0}
html,body{width:1200px;height:3327px;overflow:hidden}
body{font-family:"Lato",sans-serif;color:var(--ink);background:#fff;position:relative}
.abs{position:absolute}
a{color:inherit;text-decoration:none}

.topbar{position:absolute;left:0;top:0;width:1200px;height:41px;background:var(--green);color:#fff;font-size:15px}
.topbar .social{position:absolute;left:111px;top:11px;display:flex;gap:18px}
.topbar .contact{position:absolute;right:111px;top:11px;display:flex;gap:30px}
.ico{display:inline-block;width:14px;height:14px;background:#fff;border-radius:50%;vertical-align:-2px;margin-right:6px}

.brand{font-family:"Lato",sans-serif;font-weight:700;color:var(--lime);font-size:20px}
.brand-mark{width:52px;height:52px;border-radius:50%;background:var(--green);margin:10px 0 0 18px}

.search{left:327px;top:74px;width:484px;height:47px;border:2px solid #e4e4e4;display:flex}
.search span{flex:1;padding:14px 0 0 42px;color:#888;font-size:15px}
.search b{width:100px;background:var(--green);color:#fff;font-weight:700;font-size:16px;text-align:center;line-height:43px}
.cart{left:825px;top:74px;width:128px;height:47px;border:2px solid #e4e4e4;font-size:15px;line-height:43px;padding-left:36px}
.login{left:967px;top:74px;width:122px;height:47px;background:var(--green);color:#fff;font-weight:700;font-size:16px;line-height:47px;text-align:center;box-shadow:0 2px 4px rgba(0,0,0,.3)}

.nav{left:111px;top:152px;width:978px;height:44px;border-top:1px solid var(--line);display:flex;font-family:"Domine",serif;font-size:16px}
.nav a{padding:11px 24px 0;height:44px}
.nav a.on{border-bottom:3px solid var(--green);padding-left:62px;padding-right:26px}

.hero{left:0;top:196px;width:1200px;height:604px;background:linear-gradient(110deg,#cfd8d0 0%,#8da58a 40%,#4f6e4a 70%,#2f4a30 100%)}
.hero h1{left:111px;top:180px;font-size:88px;color:#fff;font-family:"Domine",serif;font-weight:700;letter-spacing:1px}
.hero p{left:111px;top:279px;width:500px;color:#fff;font-size:15px;line-height:26px}
.btn{background:var(--green);color:#fff;font-family:"Domine",serif;font-weight:700;font-size:15px;padding:0 16px;height:48px;line-height:48px}
.arrow{width:34px;height:34px;border-radius:50%;background:var(--green)}
.arrow.w{background:#fff}

.title{width:1200px;text-align:center;font-family:"Domine",serif;font-weight:700;font-size:38px;left:0}
.divider{left:527px;width:146px;height:20px}

.card{width:230px;height:262px;border:1px solid var(--line);box-shadow:0 1px 4px rgba(0,0,0,.12);background:#fff}
.card .img{height:188px;border-bottom:1px solid var(--line);position:relative}
.card .ph{position:absolute;left:10px;top:10px;right:10px;bottom:10px}
.off{position:absolute;left:0;top:0;width:38px;height:46px;background:var(--green);color:#fff;font-family:"Domine",serif;font-weight:700;font-size:12px;line-height:13px;padding:10px 0 0 6px}
.card h4{font-family:"Domine",serif;font-size:13px;text-align:center;margin-top:16px}
.price{text-align:center;margin-top:9px;font-size:16px}
.price s{color:#777;margin-right:18px}
.price b{color:var(--green);font-weight:400}
.hover-btn{position:absolute;left:50px;width:130px;height:38px;color:#fff;font-family:"Domine",serif;font-weight:700;font-size:13px;line-height:38px;text-align:center}

.about{left:0;top:1334px;width:1200px;height:398px;background:linear-gradient(90deg,#1f8a4c 0%,#2a9452 45%,#5e9e62 65%,#a3b8a6 100%)}
.about h2{left:106px;top:35px;color:#fff;font-family:"Domine",serif;font-size:40px}
.about p{left:106px;top:130px;width:490px;color:#fff;font-size:15px;line-height:25.7px}

.testi{width:395px;height:200px;border:2px solid var(--green);background:#fff;box-shadow:10px 10px 0 var(--green)}
.testi .q{position:absolute;left:28px;top:30px;color:var(--green);font-weight:700;font-size:22px;font-family:"Domine",serif}
.testi p{position:absolute;left:46px;top:52px;width:330px;color:#777;font-size:15px;line-height:25.7px}
.testi h5{position:absolute;left:46px;top:160px;color:var(--green);font-family:"Domine",serif;font-size:16px}
.testi h5:after{content:"";display:inline-block;width:60px;height:2px;background:var(--green);margin-left:10px;vertical-align:4px}

.blogbg{left:0;top:2233px;width:1200px;height:604px;background:var(--gray-bg)}
.bcard{background:#fff;box-shadow:0 1px 4px rgba(0,0,0,.1)}
.date{position:absolute;width:52px;height:50px;background:var(--lime);font-family:"Domine",serif;font-weight:700;text-align:center;font-size:20px;line-height:20px;padding-top:6px}
.date small{display:block;font-size:13px;font-family:"Lato",sans-serif;font-weight:400}
.meta{color:var(--green);font-size:15px}
.bcard h4{font-family:"Domine",serif;font-size:13px;line-height:20px}
.bcard p{color:#777;font-size:15px;line-height:22px}
.more{color:var(--green);font-family:"Domine",serif;font-weight:700;font-size:15px}
.featured-body{position:absolute;left:18px;top:206px;width:330px}
.featured-body h4{font-size:12px;line-height:20px;margin-top:8px;letter-spacing:-.1px}
.featured-body p{margin-top:6px;line-height:25px;font-size:14.5px}
.featured-body .more{margin-top:6px}

.news{left:0;top:2837px;width:1200px;height:107px;background:var(--green)}
.news h2{left:183px;top:30px;color:#fff;font-family:"Domine",serif;font-size:38px}
.news .field{left:610px;top:35px;width:260px;height:42px;border:1px solid #fff;color:#fff;font-family:"Domine",serif;font-size:14px;line-height:40px;padding-left:12px}
.news .sub{left:885px;top:35px;width:133px;height:42px;background:#fff;color:var(--green);font-family:"Domine",serif;font-weight:700;font-size:14px;line-height:42px;text-align:center}

.footer{left:0;top:2944px;width:1200px;height:383px;background:var(--footer);color:#fff}
.footer h3{font-family:"Domine",serif;font-size:17px}
.footer ul{list-style:none;font-size:15px;line-height:34px;margin-top:18px}
.fcircle{width:32px;height:32px;border-radius:50%;background:var(--green);flex:none}
.footer .row{display:flex;align-items:center;gap:12px;font-size:15px;line-height:21px}
.copy{left:111px;top:334px;width:978px;border-top:1px solid #444;text-align:center;padding-top:20px;font-size:15px}
</style>
</head>
<body>

<div class="topbar">
  <div class="social"><span>f</span><span>t</span><span>in</span></div>
  <div class="contact"><span><i class="ico"></i>info@lunavetta.com</span><span><i class="ico"></i>555-0100-200</span></div>
</div>

<div class="abs" style="left:111px;top:52px">
  <div class="brand">Lunavetta</div>
  <div class="brand-mark"></div>
</div>
<div class="abs search"><span>Search Products</span><b>Search</b></div>
<div class="abs cart">My Cart <span style="color:var(--green);margin-left:10px">0</span></div>
<div class="abs login">Login →</div>

<nav class="abs nav">
  <a class="on">Home</a><a>About Us</a><a>About the Laboratory</a><a>About CBDP</a><a>About THCP</a><a>Shop</a><a>Contact Us</a>
</nav>

<section class="abs hero" role="img" aria-label="Scientist examining hemp plants with a microscope in a laboratory">
  <h1 class="abs">LUNAVETTA</h1>
  <p class="abs">Lorem ipsum dolor sit amet, consectetur adipiscing elit, sed do eiusmod tempor incididunt ut labore et dolore magna aliqua enim minim veniam.</p>
  <div class="abs btn" style="left:111px;top:359px">GET STARTED ➜</div>
  <div class="abs arrow" style="left:109px;top:507px"></div>
  <div class="abs arrow w" style="left:169px;top:507px"></div>
</section>

<h2 class="abs title" style="top:872px">OUR PRODUCTS</h2>
<svg class="abs divider" style="top:929px" viewBox="0 0 146 20"><line x1="0" y1="10" x2="50" y2="10" stroke="#1f8a4c" stroke-width="2"/><circle cx="73" cy="10" r="9" fill="#1f8a4c"/><line x1="96" y1="10" x2="146" y2="10" stroke="#1f8a4c" stroke-width="2"/></svg>

<div class="abs card" style="left:111px;top:987px">
  <div class="img">
    <div class="ph" role="img" aria-label="Product photo: yellow vape pen" style="background:linear-gradient(180deg,#fbf8e8,#f3ecc4)"></div>
    <div class="off">20%<br>OFF</div>
    <div class="abs" style="right:6px;top:6px;width:24px;height:24px;background:#eee;color:#e11;text-align:center;line-height:24px">★</div>
    <div class="hover-btn" style="top:61px;background:var(--green)">ADD TO CART</div>
    <div class="hover-btn" style="top:112px;background:var(--lime);color:#063">VIEW DETAILS</div>
  </div>
  <h4>PRODUCTS TITTLE</h4><div class="price"><s>$34.00</s><b>$30.00</b></div>
</div>
<div class="abs card" style="left:360px;top:987px">
  <div class="img"><div class="ph" role="img" aria-label="Product photo: red vape pen" style="background:linear-gradient(180deg,#fbf1f1,#f4dcdc)"></div><div class="off">20%<br>OFF</div></div>
  <h4>PRODUCTS TITTLE</h4><div class="price"><s>$34.00</s><b>$30.00</b></div>
</div>
<div class="abs card" style="left:610px;top:987px">
  <div class="img"><div class="ph" role="img" aria-label="Product photo: hemp gummies with leaves" style="background:linear-gradient(180deg,#f6f8ee,#e9eed6)"></div><div class="off">20%<br>OFF</div></div>
  <h4>PRODUCTS TITTLE</h4><div class="price"><s>$34.00</s><b>$30.00</b></div>
</div>
<div class="abs card" style="left:859px;top:987px">
  <div class="img"><div class="ph" role="img" aria-label="Product photo: amber tincture bottles" style="background:linear-gradient(180deg,#f8f3ec,#eedfcb)"></div><div class="off">20%<br>OFF</div></div>
  <h4>PRODUCTS TITTLE</h4><div class="price"><s>$34.00</s><b>$30.00</b></div>
</div>

<section class="abs about">
  <div class="abs" role="img" aria-label="Gloved hand dropping oil into a flask among hemp plants" style="left:640px;top:0;width:560px;height:398px;background:linear-gradient(90deg,rgba(42,148,82,0),#b9c8bd 60%,#d8dde0)"></div>
  <h2 class="abs">ABOUT US</h2>
  <svg class="abs" style="left:106px;top:85px" width="86" height="22" viewBox="0 0 86 22"><circle cx="11" cy="11" r="10" fill="#fff" opacity=".7"/><line x1="36" y1="11" x2="86" y2="11" stroke="#fff" stroke-width="2"/></svg>
  <p class="abs">Lorem ipsum dolor sit amet, consectetur adipiscing elit, sed do eiusmod tempor incididunt ut labore et dolore magna aliqua. Ut enim ad minim veniam, quis nostrud exercitation ullamco laboris nisi ut aliquip ex ea commodo consequat. Duis aute irure dolor in reprehenderit in voluptate velit esse cillum dolore eu fugiat nulla pariatur. Excepteur sint occaecat cupidatat non proident, sunt in culpa qui officia deserunt laborum.</p>
  <div class="abs btn" style="left:106px;top:306px;background:transparent;border:1px solid #fff">GET STARTED ➜</div>
</section>

<h2 class="abs title" style="top:1802px">OUR TESTIMONIALS</h2>
<svg class="abs divider" style="top:1855px" viewBox="0 0 146 20"><line x1="0" y1="10" x2="50" y2="10" stroke="#1f8a4c" stroke-width="2"/><circle cx="73" cy="10" r="9" fill="#1f8a4c"/><line x1="96" y1="10" x2="146" y2="10" stroke="#1f8a4c" stroke-width="2"/></svg>
<div class="abs arrow" style="left:75px;top:2019px"></div>
<div class="abs arrow" style="left:1091px;top:2019px"></div>
<div class="abs testi" style="left:177px;top:1925px;transform:rotate(-1deg)">
  <div class="q">“</div>
  <p>Lorem ipsum dolor amet, consectetur adipiscing elit, sed do eiusmod tempor incididunt ut labore dolore magna aliqua. Ut enim minim veniamquis nostrud exercitation ullamco laboris nisialiquip..</p>
  <h5>Jhon Deo</h5>
</div>
<div class="abs testi" style="left:614px;top:1925px;transform:rotate(-1deg)">
  <div class="q">“</div>
  <p>Lorem ipsum dolor amet, consectetur adipiscing elit, sed do eiusmod tempor incididunt ut labore dolore magna aliqua. Ut enim minim veniamquis nostrud exercitation ullamco laboris nisialiquip..</p>
  <h5>Jhon Smith</h5>
</div>

<section class="abs blogbg"></section>
<h2 class="abs title" style="top:2264px">LATEST BLOG</h2>
<svg class="abs divider" style="top:2320px" viewBox="0 0 146 20"><line x1="0" y1="10" x2="50" y2="10" stroke="#1f8a4c" stroke-width="2"/><circle cx="73" cy="10" r="9" fill="#1f8a4c"/><line x1="96" y1="10" x2="146" y2="10" stroke="#1f8a4c" stroke-width="2"/></svg>

<div class="abs bcard" style="left:159px;top:2373px;width:358px;height:418px">
  <div class="abs" role="img" aria-label="Gloved hands with tweezers and microscope" style="left:8px;top:8px;width:342px;height:170px;background:linear-gradient(120deg,#e0d0e8,#5a8ad8 45%,#d8d8d8)"></div>
  <div class="date" style="left:8px;top:8px">29<small>Jul</small></div>
  <div class="featured-body">
    <div class="meta">▦ &nbsp; 29 Jul 2021 &nbsp;&nbsp;&nbsp;&nbsp; ▭ &nbsp; Comments</div>
    <h4>LOREM IPSUM DOLOR CONSECTETUR ADIPISC<br>ELIT, SED DO EIUSMOD TEMPOR INCIDIDUNT UT</h4>
    <p>Lorem ipsum dolor sit amet, consectetur scing elit, sed do eiusmod tempor incididunt ut labore et dolore magna aliqua. Ut enim ad minim quis nostrud exercitation ullamco laboris nisi ut</p>
    <div class="more">READ MORE ➜</div>
  </div>
</div>

<div class="abs bcard" style="left:552px;top:2373px;width:489px;height:200px">
  <div class="abs" role="img" aria-label="Dropper over flask with hemp leaf" style="left:8px;top:8px;width:168px;height:184px;background:linear-gradient(#eef0ee,#c8d8c0)"></div>
  <div class="date" style="left:8px;top:8px">29<small>Jul</small></div>
  <h4 class="abs" style="left:196px;top:18px">LOREM IPSUM DOLOR SIT ADIPISCING</h4>
  <div class="abs meta" style="left:196px;top:49px">▦ &nbsp; 29.7.2021 &nbsp;&nbsp; ▭ Comments</div>
  <p class="abs" style="left:196px;top:78px;width:285px">Lorem ipsum dolor sit amet, consectetur adipiscing elit, sed do eiusmod tempor incididunt ut labore dolore magna aliqua.</p>
  <div class="abs more" style="left:196px;top:164px">Read More ➜</div>
</div>

<div class="abs bcard" style="left:552px;top:2590px;width:489px;height:200px">
  <div class="abs" role="img" aria-label="Lab worker in mask holding a hemp sample" style="left:8px;top:8px;width:168px;height:184px;background:linear-gradient(#4a7ab8,#e8ecef)"></div>
  <div class="date" style="left:8px;top:8px">29<small>Jul</small></div>
  <h4 class="abs" style="left:196px;top:18px">LOREM IPSUM DOLOR SIT ADIPISCING</h4>
  <div class="abs meta" style="left:196px;top:49px">▦ &nbsp; 29.7.2021 &nbsp;&nbsp; ▭ Comments</div>
  <p class="abs" style="left:196px;top:78px;width:285px">Lorem ipsum dolor sit amet, consectetur adipiscing elit, sed do eiusmod tempor incididunt ut labore dolore magna aliqua.</p>
  <div class="abs more" style="left:196px;top:164px">Read More ➜</div>
</div>

<section class="abs news">
  <h2 class="abs">NEWSLETTER</h2>
  <div class="abs field">Enter Your Email:</div>
  <div class="abs sub">SUBSCRIBE</div>
</section>

<footer class="abs footer">
  <div class="abs" style="left:108px;top:55px">
    <div class="brand">Lunavetta</div>
    <div class="brand-mark"></div>
  </div>
  <p class="abs" style="left:108px;top:160px;width:260px;font-size:15px;line-height:24px">Lorem ipsum dolor consectetur adip sed do eiusmod tempor incididunt ut labore et dolore magna aliqua.</p>
  <div class="abs" style="left:110px;top:258px;display:flex;gap:16px"><div class="fcircle"></div><div class="fcircle"></div><div class="fcircle"></div></div>

  <div class="abs" style="left:448px;top:57px">
    <h3>Quicklinks</h3>
    <ul><li>Home</li><li>About Us</li><li>About the Laboratory</li><li>About CBDP</li><li>About THCP</li><li>Shop</li><li>Contact Us</li></ul>
  </div>
  <div class="abs" style="left:683px;top:57px">
    <h3>Qtherlinks</h3>
    <ul><li>FAQ</li><li>Privacy</li><li>Services</li><li>Team</li><li>Shop</li></ul>
  </div>
  <div class="abs" style="left:863px;top:57px">
    <h3>CONTACT WITH US</h3>
    <div class="row" style="margin-top:28px"><div class="fcircle"></div>555-0100-200</div>
    <div class="row" style="margin-top:32px"><div class="fcircle"></div>info@lunavetta.com</div>
    <div class="row" style="margin-top:30px"><div class="fcircle"></div>123, Lorem ipsum dolor sit<br>consectetur adipiscing</div>
  </div>
  <div class="abs copy">©Copyrights 2021 lunavetta.com | &nbsp; All Rights Reserved |</div>
</footer>

</body>
</html>
```